Business Card Design for VELDRI Technology Partners

already have logo. I am showing existing card so you can see address/phone info this design needs to be simple,clean,creative

```html
<!DOCTYPE html>
<html lang="en">
<head>
<meta charset="utf-8">
<title>VELDRI Technology Partners – Business Card</title>
<link href="https://fonts.googleapis.com/css2?family=Source+Sans+3:wght@400;600&display=swap" rel="stylesheet">
<style>
  :root {
    --backdrop: #5b5b5b;
    --brand-blue: #0c4a7d;
    --card-white: #ffffff;
    --ink: #1f4f80;
    --ink-soft: #3f5f80;
    --card-shadow: 0 10px 26px rgba(0, 0, 0, 0.45);
  }
  * { margin: 0; padding: 0; box-sizing: border-box; }
  html, body {
    width: 1200px;
    height: 800px;
    overflow: hidden;
    background: var(--backdrop);
    font-family: "Source Sans 3", Arial, sans-serif;
  }
  .stage { position: relative; width: 1200px; height: 800px; }

  .card {
    position: absolute;
    width: 565px;
    height: 332px;
    box-shadow: var(--card-shadow);
  }

  /* Back of card */
  .card--back {
    left: 493px;
    top: 123px;
    background: var(--brand-blue);
    color: var(--card-white);
  }
  .card--back .brand {
    position: absolute;
    left: 200px;
    top: 140px;
    display: flex;
    align-items: center;
    gap: 14px;
  }
  .card--back .brand-dot {
    width: 40px; height: 40px; border-radius: 50%;
    background: var(--card-white);
  }
  .card--back .brand-name {
    font-size: 44px;
    font-weight: 400;
    letter-spacing: 1px;
    color: var(--card-white);
  }
  .services {
    position: absolute;
    right: 38px;
    top: 270px;
    text-align: right;
    font-size: 12.5px;
    line-height: 17px;
  }
  .services-tab {
    position: absolute;
    right: 0;
    top: 273px;
    width: 19px;
    height: 34px;
    background: var(--card-white);
  }

  /* Front of card */
  .card--front {
    left: 156px;
    top: 380px;
    background: var(--card-white);
  }
  .card--front .brand {
    position: absolute;
    left: 77px;
    top: 52px;
    display: flex;
    align-items: center;
    gap: 14px;
  }
  .card--front .brand-dot {
    width: 42px; height: 42px; border-radius: 50%;
    background: var(--brand-blue);
  }
  .card--front .brand-name {
    font-size: 44px;
    font-weight: 400;
    letter-spacing: 1px;
    color: var(--brand-blue);
  }
  .front-tab {
    position: absolute;
    left: 0;
    top: 276px;
    width: 19px;
    height: 33px;
    background: var(--brand-blue);
  }

  .contact-block {
    position: absolute;
    left: 311px;
    top: 123px;
    color: var(--ink);
  }
  .person-name { font-size: 19px; font-weight: 400; line-height: 22px; }
  .person-role { font-size: 13px; color: var(--ink-soft); line-height: 17px; }
  .address { margin-top: 14px; font-size: 13.5px; line-height: 18px; }
  .address .company { font-weight: 600; }
  .contact-list { margin-top: 13px; list-style: none; font-size: 13px; line-height: 19px; }
  .contact-list li { display: flex; align-items: center; gap: 6px; }
  .contact-list svg { width: 10px; height: 10px; fill: var(--ink); flex: none; }
</style>
</head>
<body>
<main class="stage">

  <section class="card card--back" aria-label="Card back">
    <div class="brand">
      <span class="brand-dot"></span>
      <span class="brand-name">VELDRI</span>
    </div>
    <p class="services">Technology Strategy<br>IT Service Management</p>
    <span class="services-tab"></span>
  </section>

  <section class="card card--front" aria-label="Card front">
    <div class="brand">
      <span class="brand-dot"></span>
      <span class="brand-name">VELDRI</span>
    </div>

    <div class="contact-block">
      <p class="person-name">Daniel Hartwell</p>
      <p class="person-role">Designation</p>
      <p class="address">
        <span class="company">Veldri Technology Services</span>,<br>
        214-c Harbor Lane, #312,<br>
        Linden Bay, Ca 90412.
      </p>
      <ul class="contact-list">
        <li>
          <svg viewBox="0 0 10 10" aria-hidden="true"><path d="M1 3.2C1 2 2 1 3.2 1h3.6C8 1 9 2 9 3.2v.6H6.8V2.8H3.2v1H1zM2 4.6h6l1 4.4H1z"/></svg>
          555.218.0440 EXT.800
        </li>
        <li>
          <svg viewBox="0 0 10 10" aria-hidden="true"><path d="M0.5 2h9v6h-9zM1.3 2.6 5 5.6l3.7-3z" fill-rule="evenodd"/></svg>
          daniel@veldri.com
        </li>
        <li>
          <svg viewBox="0 0 10 10" aria-hidden="true"><path d="M5 .5a4.5 4.5 0 1 0 0 9 4.5 4.5 0 0 0 0-9zm0 1c.7.8 1.1 2 1.2 3H3.8c.1-1 .5-2.2 1.2-3zM3.8 5.5h2.4c-.1 1-.5 2.2-1.2 3-.7-.8-1.1-2-1.2-3zM1.6 4.5c.2-1.3 1-2.3 2.1-2.8-.5.8-.8 1.8-.9 2.8zm0 1h1.2c.1 1 .4 2 .9 2.8-1.1-.5-1.9-1.5-2.1-2.8zm6.8 0c-.2 1.3-1 2.3-2.1 2.8.5-.8.8-1.8.9-2.8zm0-1H7.2c-.1-1-.4-2-.9-2.8 1.1.5 1.9 1.5 2.1 2.8z"/></svg>
          www.veldri.com
        </li>
      </ul>
    </div>

    <span class="front-tab"></span>
  </section>

</main>
</body>
</html>
```